VARLEX CONSULTING / PROJECT MANAGEMENT WEB DESIGN

Design Brief: Varlex Consulting Website

I own 'VARLEX' business name and therefore can keep the name and logo simple i.e. VARLEX only and incorporate consulting / Project Management within the design or text.

Purpose:

The purpose of this project is to create a website for Varlex.com.au, a project management consulting company. The website will promote the company's services, allowing potential clients to learn more about Varlex and its capabilities. The website should be professional, easy to navigate, and provide all necessary information for potential clients.

Target Audience:

Clients in the Oil & Gas, LNG, and Chemical industry
Businesses and organizations in need of project management and engineering consultancy services
Potential clients looking for information about the company and its services
Key Elements:
Clean and modern design that reflects the company's professional image and incorporates the company logo

Clear and easy-to-use navigation menu

“Homepage” that promotes the company's main services and includes the company's mission statement.

Services:

PROJECT MANAGEMENT
PROJECT ENGINEERING
QUALITY MANAGEMENT AND PROCESS DEVELOPMENT
BUSINESS CASE DEVELOPMENT
ENGINEERING & DESIGN MANAGEMENT
CONCEPT STUDIES AND PROJECT SUPPORT
CONSTRUCTION MANAGEMENT
CONTRACT MANAGEMENT / CLAIMS PROCUREMENT / SUPPLY CHAIN SUPPORT
COMMERCIAL LIABILITY & RISK MANAGEMENT

Mission Statement:

"Our mission at Varlex is to provide expert project management and engineering consultancy services that help our clients achieve their goals and exceed their expectations. We will accomplish this by offering a full range of services, providing experienced and highly-qualified professionals, building strong relationships with our clients, continuously improving our services, and maintaining a reputation for excellence."

"About" page that includes client-supplied text about the company
"Contact" page with an editable form, email, and phone number for potential clients to get in touch with the company

Design Style:

Professional and modern
Clean and simple layout
Use of the company's colors and branding (subject to change)
Use of high-quality images that reflect the industry and services

Functionality:
Responsive design that is optimized for all devices and screen sizes

Website will be coded and uploaded to a content management system (CMS) for easy updates and maintenance
Website will be optimized for search engines and include all necessary SEO elements
Website will be fully tested for compatibility with all modern web browsers and devices
Website will be secured with an SSL certificate to ensure the safety of user data (client hosting includes SSL certificate).

Target Market(s)

Clients in the Oil & Gas, LNG, and Chemical industry Businesses and organizations in need of project management and engineering consultancy services Potential clients looking for information about the company and its services

Industry/Entity Type

Oil & Gas, LNG, and Chemical industry Businesses and organizations

Coding

Coded - Design and coding required

Number of Pages Required

3 page

Font styles to use
Sans Serif

Colors
0054AA
0677BA
7BADD7
CADEEF
E8F1F8
EB3D1F
EC4F4E
F09395
F8D3D4
FCEDEE
6B429C
8869AF
B7A5CE
E3DAEB
F3F0F8

Requirements
Must have
• HOME ABOUT AND CONTACT PAGE
Nice to have
• Fresh look, open to ideas
Should not have
• Stock images and hand shakes and meeting rooms..

```html
<!DOCTYPE html>
<html lang="en">
<head>
<meta charset="utf-8">
<title>Varlex Resources – Project Management &amp; Engineering Consultancy</title>
<link rel="stylesheet" href="https://fonts.googleapis.com/css2?family=Poppins:ital,wght@0,300;0,400;0,500;0,600;0,700;0,800;1,400&display=swap">
<style>
:root{
  --blue:#0677BA;
  --blue-dark:#0054AA;
  --blue-mid:#7BADD7;
  --blue-soft:#CADEEF;
  --blue-pale:#E8F1F8;
  --card-tint:#DCEBF7;
  --navy:#0F2747;
  --ink:#1E1E1E;
  --text:#3A3A3A;
  --white:#FFFFFF;
  --star:#F5B800;
  --line:#D9DEE4;
}
*{box-sizing:border-box;margin:0;padding:0}
html,body{width:1200px;height:3976px;overflow:hidden}
body{font-family:'Poppins',sans-serif;color:var(--ink);background:var(--white);position:relative}
.abs{position:absolute}
section,header,footer{position:absolute;left:0;width:1200px;overflow:hidden}
.btn{position:absolute;display:flex;align-items:center;justify-content:center;border-radius:40px;background:var(--blue);color:var(--white);font-weight:500;text-transform:uppercase;white-space:nowrap}
.label{position:absolute;left:0;width:1200px;text-align:center;color:var(--blue);font-weight:600;font-size:16px;letter-spacing:.3px}
.heading{position:absolute;left:0;width:1200px;text-align:center;font-size:28px;font-weight:400;line-height:34px;color:var(--ink)}
.heading b{font-weight:700}

/* hero */
.hero{top:0;height:599px}
.hero-photo{position:absolute;inset:0;background:linear-gradient(100deg,#1b3550 0%,#2f4e68 35%,#6d7d88 60%,#a7a49f 80%,#8a8f95 100%)}
.hero-shade{position:absolute;inset:0;background:linear-gradient(90deg,rgba(8,25,45,.55) 0%,rgba(8,25,45,.2) 55%,rgba(0,0,0,0) 100%)}
.brand{position:absolute;left:113px;top:8px;width:160px;text-align:center}
.brand-mark{width:46px;height:46px;border-radius:50%;background:var(--blue);margin:0 auto}
.brand-name{margin-top:16px;color:var(--blue);font-weight:600;font-size:16px;letter-spacing:.2px}
.nav a{position:absolute;top:38px;color:var(--white);font-size:15px;font-weight:600;text-decoration:none}
.nav .active:after{content:"";position:absolute;left:0;right:0;bottom:-6px;height:2px;background:var(--white)}
.search{left:1032px;top:18px;width:54px;height:54px;border-radius:50%;background:var(--blue)}
.socials-side span{position:absolute;left:50px;width:12px;height:12px;border-radius:50%;background:var(--white)}
.scroll-down{left:22px;top:420px;transform:rotate(-90deg);transform-origin:center;color:var(--white);font-size:11px;width:100px;text-align:center}
.hero-welcome{left:110px;top:152px;color:var(--white);font-size:34px;font-weight:700}
.hero-title{left:106px;top:206px;color:var(--white);font-size:62px;font-weight:800;line-height:66px;letter-spacing:.5px}
.hero-text{left:113px;top:353px;color:var(--white);font-size:18px;line-height:26px;width:520px}
.hero-btn{left:111px;top:429px;width:192px;height:42px;font-size:15px}
.dots span{position:absolute;top:533px;width:12px;height:12px;border-radius:50%;border:1.5px solid var(--white)}
.dots .on{background:var(--blue);border-color:var(--blue)}

/* about */
.about{top:599px;height:582px;background:var(--white)}
.photo{position:absolute}
.about-label{left:608px;top:84px;color:var(--blue);font-weight:600;font-size:16px}
.about-title{left:608px;top:116px;width:520px;font-size:29px;line-height:37px;font-weight:400}
.about-title b{font-weight:700}
.about-text{left:612px;top:246px;width:490px;font-size:18px;line-height:26px;color:var(--text)}
.about-btn{left:610px;top:456px;width:142px;height:40px;font-size:14px}

/* services */
.services{top:1181px;height:649px;background:var(--blue-pale)}
.card{position:absolute;top:221px;width:232px;height:343px;background:var(--white);text-align:center}
.card.current{border-bottom:4px solid var(--blue);box-shadow:0 2px 8px rgba(0,0,0,.08)}
.card-icon{position:absolute;left:72px;top:24px;width:88px;height:88px}
.card h3{position:absolute;left:0;top:126px;width:100%;font-size:18px;line-height:26px;font-weight:600;text-transform:uppercase;color:var(--ink)}
.card.current h3{color:var(--blue)}
.card p{position:absolute;left:14px;top:184px;width:204px;font-size:14px;line-height:24px;color:var(--text)}
.card .btn{left:52px;top:276px;width:128px;height:36px;font-size:12.5px}
.arrow{position:absolute;top:1543px}

/* call to action */
.cta{top:1830px;height:597px}
.cta-photo{position:absolute;inset:0;background:linear-gradient(110deg,#3c4a55 0%,#6f7c84 35%,#9aa3a8 60%,#c9ccc9 85%,#e2e2de 100%)}
.cta-circle{position:absolute;left:111px;top:88px;width:426px;height:426px;border-radius:50%;background:var(--blue);text-align:center;color:var(--white)}
.cta-kicker{position:absolute;left:0;top:104px;width:100%;font-size:13px}
.cta-title{position:absolute;left:0;top:136px;width:100%;font-size:34px;line-height:48px;font-weight:400}
.cta-title b{font-weight:700}
.cta-sub{position:absolute;left:0;top:233px;width:100%;font-size:14px}
.cta-btn{left:122px;top:285px;width:192px;height:40px;font-size:15px;background:var(--white);color:var(--blue);font-weight:600}

/* testimonials */
.testimonials{top:2427px;height:571px;background:var(--white)}
.t-card{position:absolute;top:213px;width:309px;height:272px;background:var(--card-tint);text-align:center}
.quote{position:absolute;top:-56px;left:18px}
.t-card h4{position:absolute;left:0;top:36px;width:100%;font-size:19px;font-weight:500}
.t-card .role{position:absolute;left:0;top:66px;width:100%;font-size:13px;color:var(--text)}
.stars{position:absolute;left:0;top:90px;width:100%;display:flex;justify-content:center;gap:4px}
.t-card p{position:absolute;left:18px;top:128px;width:273px;font-size:15px;line-height:24px;color:var(--text)}
.t-dots span{position:absolute;top:2948px;width:11px;height:11px;border-radius:50%;background:var(--blue-mid)}

/* contact */
.contact{top:2998px;height:592px;background:var(--blue-pale)}
.field{position:absolute;background:var(--white);border:1px solid var(--line);font-size:14px;font-style:italic;color:#8a8a8a;padding:14px 22px}
.send{left:519px;top:465px;width:170px;height:42px;font-size:14px}

/* footer */
.footer{top:3590px;height:386px;background:var(--navy);color:var(--white)}
.f-brand{position:absolute;left:118px;top:70px;width:200px;text-align:center}
.f-brand .brand-mark{width:56px;height:56px}
.f-brand .brand-name{margin-top:18px;font-size:21px}
.f-contact{position:absolute;left:120px;font-size:16px;font-weight:500;line-height:22px}
.f-contact svg{position:absolute;left:0;top:2px}
.f-contact span{display:block;padding-left:20px}
.f-col h5{position:absolute;top:80px;font-size:21px;font-weight:600}
.f-col a{position:absolute;color:var(--white);font-size:16px;font-weight:500;text-decoration:none}
.f-news{position:absolute;left:857px;top:132px;width:240px;font-size:16px;font-weight:600;line-height:22px}
.f-input{position:absolute;left:858px;top:191px;width:227px;height:37px;background:var(--white);color:#777;font-size:13px;padding:9px 14px}
.f-btn{left:857px;top:251px;width:124px;height:41px;font-size:14px}
.f-rule{position:absolute;left:0;top:324px;width:1200px;height:1px;background:rgba(255,255,255,.2)}
.copy{position:absolute;left:113px;top:346px;font-size:12.5px}
.f-social span{position:absolute;top:348px;width:18px;height:18px;border-radius:50%;background:var(--white)}
</style>
</head>
<body>

<header class="hero">
  <div class="hero-photo" role="img" aria-label="Smiling consultant working on a laptop in a bright office"></div>
  <div class="hero-shade"></div>
  <div class="brand"><div class="brand-mark"></div><div class="brand-name">VARLEX RESOURCES</div></div>
  <nav class="nav">
    <a class="active" style="left:523px">Home</a>
    <a style="left:634px">About us</a>
    <a style="left:767px">Services</a>
    <a style="left:895px">Contact Us</a>
  </nav>
  <div class="abs search">
    <svg width="54" height="54" viewBox="0 0 54 54"><circle cx="25" cy="25" r="8" fill="none" stroke="#fff" stroke-width="2"/><line x1="31" y1="31" x2="36" y2="36" stroke="#fff" stroke-width="2" stroke-linecap="round"/></svg>
  </div>
  <svg class="abs" style="left:39px;top:181px" width="34" height="34"><circle cx="17" cy="17" r="15" fill="none" stroke="#fff" stroke-width="1.5"/></svg>
  <div class="socials-side">
    <span style="top:227px"></span><span style="top:257px"></span><span style="top:289px"></span>
  </div>
  <div class="abs scroll-down">SCROLL DOWN</div>
  <svg class="abs" style="left:50px;top:480px" width="12" height="26"><line x1="6" y1="0" x2="6" y2="24" stroke="#fff" stroke-width="1.2"/><polyline points="1,19 6,24 11,19" fill="none" stroke="#fff" stroke-width="1.2"/></svg>
  <div class="abs hero-welcome">Welcome to</div>
  <div class="abs hero-title">VARLEX<br>RESOURCES</div>
  <p class="abs hero-text">Popularised in the 1960s with the release of Letraset sheets containing Lorem Ipsum passages</p>
  <div class="btn hero-btn">Get started now</div>
  <div class="dots">
    <span style="left:116px"></span><span class="on" style="left:136px"></span><span style="left:156px"></span><span style="left:176px"></span>
  </div>
</header>

<section class="about">
  <div class="photo" style="left:110px;top:85px;width:224px;height:178px;background:linear-gradient(135deg,#dfe6ee,#8da4bb)" role="img" aria-label="Engineer reviewing plans on a desk"></div>
  <div class="photo" style="left:358px;top:85px;width:224px;height:178px;background:linear-gradient(135deg,#c9d4dc,#56697a)" role="img" aria-label="Project schedule on a computer monitor"></div>
  <div class="photo" style="left:110px;top:286px;width:472px;height:210px;background:linear-gradient(110deg,#6b4a34,#a4764f 45%,#3d4048 80%,#23272d)" role="img" aria-label="Smiling professional in a suit in an office"></div>
  <div class="abs about-label">ABOUT US</div>
  <h2 class="abs about-title">Our mission at <b>Varlex is to provide expert project management and engineering consultancy</b> services</h2>
  <p class="abs about-text">That help our clients achieve their goals and exceed their expectations. We will accomplish this by offering a full range of services, providing experienced and highly-qualified professionals, building strong relationships with our clients, continuously improving our services, and maintaining a reputation for excellence.</p>
  <div class="btn about-btn">Learn more</div>
</section>

<section class="services">
  <div class="label" style="top:86px">OUR SERVICES</div>
  <h2 class="heading" style="top:118px"><b>Varlex</b> is All We Do<br>That’s It</h2>

  <div class="card" style="left:111px">
    <svg class="card-icon" viewBox="0 0 88 88"><circle cx="40" cy="44" r="36" fill="var(--blue-mid)"/><rect x="30" y="10" width="40" height="52" rx="3" fill="#fff" stroke="var(--navy)" stroke-width="2.5"/><line x1="38" y1="22" x2="62" y2="22" stroke="var(--navy)" stroke-width="2.5"/><line x1="38" y1="30" x2="62" y2="30" stroke="var(--navy)" stroke-width="2.5"/><circle cx="66" cy="62" r="12" fill="var(--blue)" stroke="var(--navy)" stroke-width="2.5"/><circle cx="66" cy="62" r="4" fill="#fff"/></svg>
    <h3>Project<br>Management</h3>
    <p>It has survived not only five centuries, but also the leap into electronic typesetting.</p>
    <div class="btn">Learn more</div>
  </div>
  <div class="card current" style="left:358px">
    <svg class="card-icon" viewBox="0 0 88 88"><circle cx="40" cy="44" r="36" fill="var(--blue-mid)"/><rect x="26" y="8" width="42" height="66" rx="3" fill="#fff" stroke="var(--navy)" stroke-width="2.5"/><circle cx="47" cy="32" r="10" fill="var(--blue)" stroke="var(--navy)" stroke-width="2.5"/><circle cx="47" cy="32" r="3.5" fill="#fff"/><line x1="34" y1="54" x2="60" y2="54" stroke="var(--navy)" stroke-width="2.5"/><line x1="34" y1="62" x2="60" y2="62" stroke="var(--navy)" stroke-width="2.5"/></svg>
    <h3>Project<br>Engineering</h3>
    <p>It has survived not only five centuries, but also the leap into electronic typesetting.</p>
    <div class="btn">Learn more</div>
  </div>
  <div class="card" style="left:605px">
    <svg class="card-icon" viewBox="0 0 88 88"><circle cx="40" cy="44" r="36" fill="var(--blue-mid)"/><circle cx="56" cy="40" r="18" fill="var(--blue)" stroke="var(--navy)" stroke-width="2.5"/><rect x="28" y="34" width="24" height="38" fill="#fff" stroke="var(--navy)" stroke-width="2.5"/><line x1="34" y1="44" x2="46" y2="44" stroke="var(--navy)" stroke-width="2.5"/><line x1="34" y1="52" x2="46" y2="52" stroke="var(--navy)" stroke-width="2.5"/><line x1="34" y1="60" x2="46" y2="60" stroke="var(--navy)" stroke-width="2.5"/><line x1="22" y1="16" x2="22" y2="34" stroke="var(--navy)" stroke-width="2.5"/><line x1="14" y1="18" x2="50" y2="18" stroke="var(--navy)" stroke-width="2.5"/></svg>
    <h3>Construction<br>Management</h3>
    <p>It has survived not only five centuries, but also the leap into electronic typesetting.</p>
    <div class="btn">Learn more</div>
  </div>
  <div class="card" style="left:854px">
    <svg class="card-icon" viewBox="0 0 88 88"><circle cx="40" cy="44" r="36" fill="var(--blue-mid)"/><circle cx="38" cy="36" r="20" fill="var(--blue)" stroke="var(--navy)" stroke-width="2.5"/><rect x="30" y="50" width="8" height="20" fill="#fff" stroke="var(--navy)" stroke-width="2.5"/><rect x="42" y="42" width="8" height="28" fill="#fff" stroke="var(--navy)" stroke-width="2.5"/><rect x="54" y="34" width="8" height="36" fill="#fff" stroke="var(--navy)" stroke-width="2.5"/><polyline points="64,28 70,14 76,28" fill="none" stroke="var(--navy)" stroke-width="2.5"/></svg>
    <h3>Business Case<br>Development</h3>
    <p>It has survived not only five centuries, but also the leap into electronic typesetting.</p>
    <div class="btn">Learn more</div>
  </div>
  <svg class="abs" style="left:48px;top:362px" width="32" height="32"><circle cx="16" cy="16" r="14" fill="none" stroke="var(--blue)" stroke-width="1.6"/><polyline points="18,10 12,16 18,22" fill="none" stroke="var(--blue)" stroke-width="1.6"/></svg>
  <svg class="abs" style="left:1117px;top:362px" width="32" height="32"><circle cx="16" cy="16" r="14" fill="none" stroke="var(--blue)" stroke-width="1.6"/><polyline points="14,10 20,16 14,22" fill="none" stroke="var(--blue)" stroke-width="1.6"/></svg>
</section>

<section class="cta">
  <div class="cta-photo" role="img" aria-label="Consultant reviewing documents beside a laptop"></div>
  <div class="cta-circle">
    <div class="cta-kicker">GET STARTED NOW</div>
    <h2 class="cta-title">WE Are <b>Specialze</b><br>in Unique <b>Services</b></h2>
    <div class="cta-sub">Get Your Personal offer Within 4 Hours</div>
    <div class="btn cta-btn">Get started now</div>
  </div>
</section>

<section class="testimonials">
  <div class="label" style="top:88px">TESTIMONIALS</div>
  <h2 class="heading" style="top:116px">Our <b>Customers</b> Says</h2>

  <div class="t-card" style="left:113px">
    <svg class="quote" width="64" height="56" viewBox="0 0 64 56"><path d="M2 56V30C2 14 10 4 26 0v10c-8 3-11 8-11 16h11v30zM36 56V30C36 14 44 4 60 0v10c-8 3-11 8-11 16h11v30z" fill="var(--blue)"/></svg>
    <h4>Mark Ellison</h4><div class="role">Senior Manager</div>
    <div class="stars"><svg width="120" height="22" viewBox="0 0 120 22"><g fill="var(--star)"><polygon id="s" points="11,1 14,8 21,8 15.5,13 17.5,21 11,16.5 4.5,21 6.5,13 1,8 8,8"/><use href="#s" x="24"/><use href="#s" x="48"/><use href="#s" x="72"/><use href="#s" x="96"/></g></svg></div>
    <p>It was popularised in the 1960s with the release of Letraset sheets containing Lorem Ipsum passages, and more recently with desktop publishing software like</p>
  </div>
  <div class="t-card" style="left:446px">
    <svg class="quote" width="64" height="56" viewBox="0 0 64 56"><path d="M2 56V30C2 14 10 4 26 0v10c-8 3-11 8-11 16h11v30zM36 56V30C36 14 44 4 60 0v10c-8 3-11 8-11 16h11v30z" fill="var(--blue)"/></svg>
    <h4>Daniel Reyes</h4><div class="role">Technical Expert</div>
    <div class="stars"><svg width="120" height="22" viewBox="0 0 120 22"><g fill="var(--star)"><use href="#s"/><use href="#s" x="24"/><use href="#s" x="48"/><use href="#s" x="72"/><use href="#s" x="96"/></g></svg></div>
    <p>It was popularised in the 1960s with the release of Letraset sheets containing Lorem Ipsum passages, and more recently with desktop publishing software like</p>
  </div>
  <div class="t-card" style="left:778px">
    <svg class="quote" width="64" height="56" viewBox="0 0 64 56"><path d="M2 56V30C2 14 10 4 26 0v10c-8 3-11 8-11 16h11v30zM36 56V30C36 14 44 4 60 0v10c-8 3-11 8-11 16h11v30z" fill="var(--blue)"/></svg>
    <h4>Priya Nair</h4><div class="role">Client</div>
    <div class="stars"><svg width="120" height="22" viewBox="0 0 120 22"><g fill="var(--star)"><use href="#s"/><use href="#s" x="24"/><use href="#s" x="48"/><use href="#s" x="72"/><use href="#s" x="96"/></g></svg></div>
    <p>It was popularised in the 1960s with the release of Letraset sheets containing Lorem Ipsum passages, and more recently with desktop publishing software like</p>
  </div>
  <div class="t-dots">
    <span style="left:568px;top:521px;background:var(--blue)"></span><span style="left:594px;top:521px"></span><span style="left:620px;top:521px"></span>
  </div>
</section>

<section class="contact">
  <div class="label" style="top:84px">CONTACT</div>
  <h2 class="heading" style="top:112px">Get In <b>Touch</b> With Us</h2>
  <div class="field" style="left:190px;top:184px;width:403px;height:48px">First Name</div>
  <div class="field" style="left:604px;top:184px;width:403px;height:48px">Last Name</div>
  <div class="field" style="left:190px;top:243px;width:403px;height:48px">Email Address</div>
  <div class="field" style="left:604px;top:243px;width:403px;height:48px">Contact Number</div>
  <div class="field" style="left:190px;top:303px;width:817px;height:130px">Type Your Message Here</div>
  <div class="btn send">Send message</div>
</section>

<footer class="footer">
  <div class="f-brand"><div class="brand-mark"></div><div class="brand-name">VARLEX RESOURCES</div></div>
  <div class="f-contact" style="top:180px">
    <svg width="14" height="18" viewBox="0 0 14 18"><path d="M7 0a7 7 0 0 0-7 7c0 5 7 11 7 11s7-6 7-11a7 7 0 0 0-7-7z" fill="#fff"/><circle cx="7" cy="7" r="2.5" fill="var(--navy)"/></svg>
    <span style="padding-left:21px">18 Harbour Lane,<br>WA 6000</span>
  </div>
  <div class="f-contact" style="top:232px">
    <svg width="16" height="12" viewBox="0 0 16 12"><rect width="16" height="12" rx="1.5" fill="#fff"/><polyline points="1,1 8,7 15,1" fill="none" stroke="var(--navy)" stroke-width="1.5"/></svg>
    <span style="padding-left:20px">info@varlexconsulting.example</span>
  </div>
  <div class="f-contact" style="top:269px">
    <svg width="14" height="18" viewBox="0 0 14 18"><path d="M3 0l3 4-2 2c1 3 3 5 5 7l2-2 3 3-2 3C5 17-1 8 1 2z" fill="#fff"/></svg>
    <span style="padding-left:21px">+61 400 555 210</span>
  </div>

  <div class="f-col">
    <h5 style="left:426px">QUICK LINKS</h5>
    <a style="left:427px;top:134px">Home</a><a style="left:427px;top:168px">About Us</a><a style="left:427px;top:202px">Services</a><a style="left:427px;top:236px">Testmonials</a><a style="left:427px;top:270px">Contact Us</a>
  </div>
  <div class="f-col">
    <h5 style="left:636px">MORE INFO</h5>
    <a style="left:637px;top:134px">Blogs</a><a style="left:637px;top:168px">Privacy Policy</a><a style="left:637px;top:202px">Terms &amp; Condition</a><a style="left:637px;top:236px">Help &amp; Support</a><a style="left:637px;top:270px">Site Map</a>
  </div>
  <div class="f-col"><h5 style="left:857px">NEWSLETTER</h5></div>
  <div class="f-news">Get latest News and Never miss Updates.</div>
  <div class="f-input">Email Address</div>
  <div class="btn f-btn">Subscribe</div>

  <div class="f-rule"></div>
  <div class="copy">© Copyright 2023 Varlex Resources.</div>
  <div class="f-social"><span style="left:945px"></span><span style="left:983px"></span><span style="left:1021px"></span><span style="left:1059px"></span></div>
</footer>

</body>
</html>
```